Record Label Needs Design for CD Case, Booklet, and CD...

We are a christian record label looking to make a difference in this world.

We need 3 files -
The front and back of CD case and the actual CD graphics.

It is entitled

"Halvane Sound and Friends Summer Sampler 2014"

We will give you the artists and songs on the CD.

Please send IDEAS WE ARE OPEN TO ANYTHING!!!

you can find information on our record label at www.halvanesound.com or www.facebook.com/halvanesound

The 2 artists on the summer sampler are Marrowfen - and Copper Harbour

I have pictures of Marrowfen attached below, and pictures of copper harbour below...

marrowfenmusic.com has their logo
copper harbours logo is attached...

This is a guaranteed payout and Ive had much luck with pixel guild. Looking forward to another successful contest.

dale@halvanesound.com

Reason: We haven't had any responses yet so we extended this out a few days!

Reason: We need better designs...

Come on guys!  Send in some new designs!  I am not hard to please!  I just updated the color schemes, etc....

Target Market(s)

Christians

Industry/Entity Type

Artists

Colors
d3a5cc
ed9dc4
8768ae

Requirements
Must have
• Positivity
Nice to have
• Doves are nice
Should not have
• Crosses

```html
<!DOCTYPE html>
<html lang="en">
<head>
<meta charset="utf-8">
<title>Halvane Sound and Friends Summer Sampler 2014 – CD Artwork</title>
<link rel="stylesheet" href="https://fonts.googleapis.com/css2?family=Dancing+Script:wght@700&family=Courgette&display=swap">
<style>
  :root {
    --cyan-light: #3fe3ef;
    --cyan-mid: #16bfd6;
    --cyan-deep: #0a7f98;
    --navy: #0b2b48;
    --navy-ink: #0d3550;
    --band-blue: #0f5f86;
    --quote-accent: #7fdcf2;
    --white: #ffffff;
    --tile-black: #05070c;
    --disc-purple: #4a2f7a;
    --disc-violet: #8768ae;
    --disc-pink: #d3a5cc;
  }
  * { box-sizing: border-box; margin: 0; padding: 0; }
  html, body { width: 1200px; height: 562px; overflow: hidden; background: #ffffff; }
  .artwork { position: relative; width: 1200px; height: 562px; }

  /* Front cover */
  .front-cover {
    position: absolute; left: 0; top: 0; width: 397px; height: 562px; overflow: hidden;
    background: radial-gradient(ellipse at 75% 20%, var(--cyan-light) 0%, var(--cyan-mid) 45%, var(--cyan-deep) 100%);
  }
  .title-box {
    position: absolute; left: 22px; top: 23px; width: 354px; height: 262px;
    border: 4px solid var(--navy-ink); border-radius: 28px;
    background: linear-gradient(160deg, rgba(120,240,250,.55), rgba(20,170,195,.35));
    font-family: "Dancing Script", cursive; font-weight: 700; color: var(--navy-ink);
  }
  .title-box span { position: absolute; white-space: nowrap; line-height: 1; }
  .title-label { left: 22px; top: 16px; font-size: 32px; }
  .title-friends { left: 88px; top: 50px; font-size: 44px; }
  .title-summer { left: 22px; top: 98px; font-size: 50px; color: var(--white); }
  .title-sampler { left: 152px; top: 148px; font-size: 40px; color: var(--white); }
  .title-year { left: 162px; top: 188px; font-size: 60px; color: var(--white); }
  .dove-art {
    position: absolute; left: 30px; top: 318px; width: 175px; height: 130px;
    border-radius: 50%;
    background: radial-gradient(ellipse at center, rgba(255,255,255,.9) 0%, rgba(220,235,240,.6) 45%, rgba(255,255,255,0) 72%);
  }
  .front-tree-medallion {
    position: absolute; left: 162px; top: 318px; width: 272px; height: 272px;
    border-radius: 50%; border: 10px solid var(--white);
    background: conic-gradient(from 200deg, #f0e03a, #ff7a1a, #f0263a, #e21d8f, #7a3bd6, #2c6fe0, #3fd06a, #a6e23a, #f0e03a);
  }

  /* Back cover */
  .back-cover {
    position: absolute; left: 397px; top: 0; width: 398px; height: 562px; overflow: hidden;
    background: var(--navy);
  }
  .tagline {
    position: absolute; left: 0; top: 26px; width: 100%; text-align: center;
    font-family: "Courgette", cursive; font-size: 25px; line-height: 29px; color: var(--white);
  }
  .tagline .accent { color: var(--quote-accent); }
  .back-tree-art {
    position: absolute; left: 17px; top: 125px; width: 369px; height: 330px;
    border-radius: 48% 48% 40% 40%;
    background: conic-gradient(from 220deg at 50% 55%, #3fd06a, #2c6fe0, #7a3bd6, #f0e03a, #ff7a1a, #f0263a, #e21d8f, #3fbfd0, #3fd06a);
  }
  .label-band {
    position: absolute; left: 0; top: 452px; width: 100%; height: 110px;
    background: var(--band-blue);
  }
  .name-tile {
    position: absolute; display: flex; align-items: center; justify-content: center; text-align: center;
    background: var(--tile-black); border-radius: 10px;
    font-family: "Dancing Script", cursive; font-weight: 700; color: var(--white); line-height: 1.05;
  }
  .back-cover .tile-label { left: 25px; top: 13px; width: 117px; height: 77px; font-size: 22px; }
  .back-cover .tile-marrowfen { left: 153px; top: 30px; width: 119px; height: 45px; font-size: 22px; }
  .back-cover .tile-harbour { left: 281px; top: 15px; width: 85px; height: 75px; font-size: 20px; }

  /* Disc */
  .disc {
    position: absolute; left: 848px; top: 58px; width: 352px; height: 352px;
    border-radius: 50%; overflow: hidden;
    background: linear-gradient(115deg, #2a1a45 0%, var(--disc-purple) 40%, var(--disc-violet) 75%, var(--disc-pink) 100%);
  }
  .disc-photo { position: absolute; inset: 0; }
  .disc-band {
    position: absolute; left: 0; top: 220px; width: 100%; height: 62px;
    background: rgba(15,70,120,.75);
  }
  .disc .tile-label { left: 52px; top: 228px; width: 82px; height: 48px; font-size: 15px; }
  .disc .tile-marrowfen { left: 144px; top: 236px; width: 86px; height: 34px; font-size: 16px; }
  .disc .tile-harbour { left: 240px; top: 226px; width: 62px; height: 52px; font-size: 14px; }
  .disc-ring {
    position: absolute; left: 136px; top: 136px; width: 80px; height: 80px; border-radius: 50%;
    background: rgba(210,200,235,.55);
  }
  .disc-hole {
    position: absolute; left: 153px; top: 153px; width: 46px; height: 46px; border-radius: 50%;
    background: #ffffff;
  }
</style>
</head>
<body>
<main class="artwork">
  <section class="front-cover">
    <h1 class="title-box" aria-label="Halvane Sound and Friends Summer Sampler 2014">
      <span class="title-label">Halvane Sound</span>
      <span class="title-friends">&amp; Friends</span>
      <span class="title-summer">Summer</span>
      <span class="title-sampler">Sampler</span>
      <span class="title-year">2014</span>
    </h1>
    <div class="dove-art" role="img" aria-label="White dove in flight"></div>
    <div class="front-tree-medallion" role="img" aria-label="Rainbow-coloured tree illustration in a white-ringed circle"></div>
  </section>

  <section class="back-cover">
    <p class="tagline">if you can't get a miracle,<br><span class="accent">become one.<br>be the difference.</span></p>
    <div class="back-tree-art" role="img" aria-label="Rainbow paint-splash tree with dark branches"></div>
    <div class="label-band">
      <div class="name-tile tile-label">Halvane Sound</div>
      <div class="name-tile tile-marrowfen">Marrowfen</div>
      <div class="name-tile tile-harbour">Copper Harbour</div>
    </div>
  </section>

  <section class="disc">
    <div class="disc-photo" role="img" aria-label="Purple-toned live photo of two singers performing at microphones"></div>
    <div class="disc-band"></div>
    <div class="name-tile tile-label">Halvane Sound</div>
    <div class="name-tile tile-marrowfen">Marrowfen</div>
    <div class="name-tile tile-harbour">Copper Harbour</div>
    <div class="disc-ring"></div>
    <div class="disc-hole"></div>
  </section>
</main>
</body>
</html>
```